Personal Injury Law Firm needs folder design

Need a folder design for our personal injury law firm, Horton & Quill, LLC. to give to all of our clients with their documents at the end of their case. I've attached our branding guide. We are branded as the 5 star law firm that fights for our clients like family. It should incorporate our colors or Green and White. We'd like to convey a message of moving on to the next chapter after finishing their case.

```html
<!DOCTYPE html>
<html lang="en">
<head>
<meta charset="utf-8">
<title>Horton &amp; Quill, LLC – Client Folder</title>
<link href="https://fonts.googleapis.com/css2?family=Montserrat:ital,wght@0,400;0,600;0,800;1,600&family=Open+Sans:wght@400;600&display=swap" rel="stylesheet">
<style>
  :root{
    --green:#22a67b;
    --green-dark:#1a8a65;
    --white:#ffffff;
    --paper:#fbfbfb;
    --stage:#e8e9e9;
    --gold:#f4c430;
    --photo-a:#b7c4c9;
    --photo-b:#5f6e78;
  }
  *{box-sizing:border-box;margin:0;padding:0}
  html,body{width:1200px;height:2540px;overflow:hidden}
  body{background:var(--stage);font-family:"Open Sans",Arial,sans-serif;position:relative}

  .spread{position:absolute;left:80px;width:1040px;height:693px;display:flex;box-shadow:0 6px 24px rgba(0,0,0,.12)}
  .spread--outside{top:497px}
  .spread--inside{top:1350px}
  .panel{position:relative;width:520px;height:693px;overflow:hidden}

  /* outside */
  .panel--back,.panel--front{background:var(--green);color:var(--white)}
  .panel--back{border-right:1px solid var(--green-dark)}
  .tagline{position:absolute;left:70px;top:300px;width:380px;text-align:center}
  .tagline__quote{font-family:"Montserrat",sans-serif;font-style:italic;font-weight:600;font-size:24px}
  .tagline__stars{display:flex;justify-content:center;gap:4px;margin:12px 0 6px}
  .tagline__label{font-family:"Montserrat",sans-serif;font-weight:800;font-size:15px;letter-spacing:2px}
  .contact{position:absolute;left:40px;top:480px;list-style:none;font-size:11px;line-height:1.9}
  .contact li{display:flex;align-items:center;gap:8px}
  .fineprint{position:absolute;left:0;right:0;bottom:24px;text-align:center;font-size:9px;opacity:.85;letter-spacing:.5px}

  .brand{position:absolute;left:36px;top:36px;background:var(--white);padding:10px 16px;display:flex;align-items:center;gap:10px}
  .brand__mark{width:22px;height:22px;background:var(--green)}
  .brand__name{font-family:"Montserrat",sans-serif;font-weight:800;font-size:16px;color:var(--green)}
  .headline{position:absolute;right:36px;top:130px;width:360px;text-align:right}
  .headline__title{font-family:"Montserrat",sans-serif;font-weight:800;font-size:30px;line-height:1.15}
  .headline__sub{margin-top:10px;font-size:13px;font-weight:600;line-height:1.4}
  .photo{background:linear-gradient(160deg,var(--photo-a),var(--photo-b))}
  .photo--cover{position:absolute;right:0;bottom:0;width:330px;height:330px}

  /* inside */
  .panel--inner{background:var(--paper)}
  .panel--inner-left{border-right:1px solid #ddd}
  .pocket{position:absolute;left:0;bottom:0;width:520px;height:300px}
  .pocket svg{position:absolute;inset:0}
  .inner-brand{position:absolute;left:0;right:0;top:44px;display:flex;justify-content:center;align-items:center;gap:10px}
  .photo--team{position:absolute;left:70px;top:110px;width:380px;height:220px}
  .story{position:absolute;left:44px;right:44px;bottom:40px;color:var(--white)}
  .story__title{font-family:"Montserrat",sans-serif;font-weight:800;font-size:18px;letter-spacing:1px;margin-bottom:10px}
  .story__text{font-size:11.5px;line-height:1.6}
</style>
</head>
<body>

<section class="spread spread--outside">
  <div class="panel panel--back">
    <div class="tagline">
      <p class="tagline__quote">“Fighting for You Like Family”</p>
      <div class="tagline__stars">
        <svg width="110" height="20" viewBox="0 0 110 20" aria-hidden="true">
          <g fill="var(--gold)">
            <polygon points="10,1 12.6,7 19,7.4 14,11.6 15.6,18 10,14.5 4.4,18 6,11.6 1,7.4 7.4,7"/>
            <polygon transform="translate(22 0)" points="10,1 12.6,7 19,7.4 14,11.6 15.6,18 10,14.5 4.4,18 6,11.6 1,7.4 7.4,7"/>
            <polygon transform="translate(44 0)" points="10,1 12.6,7 19,7.4 14,11.6 15.6,18 10,14.5 4.4,18 6,11.6 1,7.4 7.4,7"/>
            <polygon transform="translate(66 0)" points="10,1 12.6,7 19,7.4 14,11.6 15.6,18 10,14.5 4.4,18 6,11.6 1,7.4 7.4,7"/>
            <polygon transform="translate(88 0)" points="10,1 12.6,7 19,7.4 14,11.6 15.6,18 10,14.5 4.4,18 6,11.6 1,7.4 7.4,7"/>
          </g>
        </svg>
      </div>
      <p class="tagline__label">5 STAR LAW FIRM</p>
    </div>
    <ul class="contact">
      <li><svg width="12" height="12" viewBox="0 0 12 12" aria-hidden="true"><path d="M6 0a4 4 0 0 1 4 4c0 3-4 8-4 8S2 7 2 4a4 4 0 0 1 4-4z" fill="#fff"/></svg>1200 Meadow Ridge Blvd, Suite 300, Denver, CO 80202</li>
      <li><svg width="12" height="12" viewBox="0 0 12 12" aria-hidden="true"><path d="M2 0h3l1 3-2 1a7 7 0 0 0 4 4l1-2 3 1v3a2 2 0 0 1-2 2C5 12 0 7 0 2a2 2 0 0 1 2-2z" fill="#fff"/></svg>(555) 014-2290</li>
      <li><svg width="12" height="12" viewBox="0 0 12 12" aria-hidden="true"><rect x="0" y="2" width="12" height="8" fill="#fff"/><path d="M0 2l6 5 6-5" stroke="var(--green)" fill="none"/></svg>hello@hortonquill.com</li>
      <li><svg width="12" height="12" viewBox="0 0 12 12" aria-hidden="true"><circle cx="6" cy="6" r="5.5" fill="none" stroke="#fff"/><path d="M0.5 6h11M6 0.5v11" stroke="#fff"/></svg>www.hortonquill.com</li>
    </ul>
    <p class="fineprint">Horton &amp; Quill, LLC · Personal Injury Attorneys · Serving Families Since 2001</p>
  </div>

  <div class="panel panel--front">
    <div class="brand"><span class="brand__mark"></span><span class="brand__name">Horton &amp; Quill, LLC</span></div>
    <div class="headline">
      <h1 class="headline__title">OUR UNIQUE VALUE PROPOSITION:</h1>
      <p class="headline__sub">Where Compassion Meets Legal Excellence in Personal Injury Advocacy</p>
    </div>
    <div class="photo photo--cover" role="img" aria-label="Photo of the firm's attorneys standing together"></div>
  </div>
</section>

<section class="spread spread--inside">
  <div class="panel panel--inner panel--inner-left">
    <div class="pocket">
      <svg width="520" height="300" viewBox="0 0 520 300" aria-hidden="true">
        <path d="M0 40 Q260 -10 520 40 V300 H0 Z" fill="var(--green)"/>
      </svg>
    </div>
  </div>
  <div class="panel panel--inner">
    <div class="inner-brand"><span class="brand__mark"></span><span class="brand__name">Horton &amp; Quill, LLC</span></div>
    <div class="photo photo--team" role="img" aria-label="Group photo of the legal team"></div>
    <div class="pocket">
      <svg width="520" height="300" viewBox="0 0 520 300" aria-hidden="true">
        <path d="M0 40 Q260 -10 520 40 V300 H0 Z" fill="var(--green)"/>
      </svg>
      <div class="story">
        <h2 class="story__title">OUR STORY</h2>
        <p class="story__text">Horton &amp; Quill began with a simple promise: treat every client like family. For over two decades we have guided injured people through difficult times, fighting for fair results so they can close this chapter and move forward with confidence.</p>
      </div>
    </div>
  </div>
</section>

</body>
</html>
```